Flyer-Design für Schädlingsbekämpfung
Zielgruppe
Schädlingsbekämpfung- und Prophylaxe, Service Monitoring, Gastronomie und Industrie, alle Lebendsmittel verarbeitenden Betriebe
Aufgabenstellung
Schwerpunkt soll das HACCP Konzept sein, welches bei allen Lebensmittelverarbeiteten Betrieben gesetzlich vorgeschrieben ist,

```html
<!DOCTYPE html>
<html lang="de">
<head>
<meta charset="utf-8">
<title>Flyer Schädlingsbekämpfung – HACCP Service</title>
<link href="https://fonts.googleapis.com/css2?family=Barlow:ital,wght@0,400;0,600;0,700;1,600;1,700&family=Barlow+Condensed:wght@400;500;600;700&display=swap" rel="stylesheet">
<style>
  :root{
    --green:#12874a;
    --green-dark:#0e7a41;
    --ink:#3f3f41;
    --text:#2b2b2b;
    --white:#ffffff;
    --stage:#f7f7f7;
  }
  *{box-sizing:border-box;margin:0;padding:0}
  html,body{width:1200px;height:817px;overflow:hidden;background:var(--stage)}
  body{font-family:"Barlow",sans-serif;color:var(--text);position:relative}
  .icon-defs{position:absolute;width:0;height:0}

  .flyer{position:absolute;top:48px;width:340px;height:720px;background:var(--white);overflow:hidden;box-shadow:0 6px 18px rgba(0,0,0,.12)}
  .flyer--haccp{left:215px}
  .flyer--services{left:645px}

  /* brand */
  .brand{position:absolute;display:flex;align-items:center;gap:8px}
  .brand__name{font-family:"Barlow",sans-serif;font-weight:400;color:var(--green);line-height:1.05;text-align:right;text-transform:uppercase}
  .brand__mark{border-radius:50%;background:var(--green);flex:none}
  .flyer--haccp .brand{top:18px;right:14px}
  .flyer--haccp .brand__name{font-size:13px}
  .flyer--haccp .brand__mark{width:58px;height:58px}
  .flyer--services .brand{top:28px;right:22px}
  .flyer--services .brand__name{font-size:17px}
  .flyer--services .brand__mark{width:72px;height:72px}

  .photo{position:absolute}

  /* HACCP flyer */
  .haccp__hero{left:0;top:0;width:340px;height:235px;background:linear-gradient(135deg,#e9eceb 0%,#f6f6f5 45%,#dfe3e2 100%)}
  .haccp__band{position:absolute;left:0;top:200px;width:340px;height:400px;background:var(--green)}
  .haccp__title{position:absolute;left:150px;top:118px;width:200px;height:112px;background:var(--green);border:4px solid var(--white);border-right:none;border-radius:34px 0 0 34px;display:flex;align-items:center;padding-left:24px;font-family:"Barlow Condensed",sans-serif;font-weight:700;color:var(--white);font-size:38px;line-height:.95}
  .haccp__intro{position:absolute;left:22px;top:236px;width:300px;color:var(--white)}
  .haccp__intro h2{font-family:"Barlow",sans-serif;font-weight:700;font-style:italic;font-size:19px;margin-bottom:6px}
  .haccp__intro p{font-family:"Barlow Condensed",sans-serif;font-size:11.5px;line-height:1.45}
  .haccp__steps{position:absolute;left:26px;top:425px;width:314px;height:170px;background:var(--ink);border-radius:26px 0 0 26px;padding:16px 14px 0 18px;color:var(--white)}
  .haccp__steps h3{font-family:"Barlow Condensed",sans-serif;font-weight:700;font-style:italic;font-size:15px;margin-bottom:6px}
  .haccp__steps li{list-style:none;font-family:"Barlow Condensed",sans-serif;font-size:11.5px;line-height:1.48}
  .haccp__benefits{position:absolute;left:22px;top:615px;width:300px;display:flex;gap:16px}
  .benefit{display:flex;gap:6px;font-family:"Barlow Condensed",sans-serif;font-weight:500;font-size:12.5px;line-height:1.25;color:var(--text)}
  .benefit svg{width:20px;height:20px;flex:none;color:var(--green)}
  .footer-bar{position:absolute;left:0;bottom:0;width:340px;height:32px;background:var(--ink);border-radius:22px 0 0 0;color:var(--white);font-weight:700;font-size:12px;display:flex;align-items:center;justify-content:center;letter-spacing:.3px}

  /* services flyer */
  .services__lead{position:absolute;left:22px;top:138px;font-weight:700;font-size:16px;color:var(--text)}
  .services__list{position:absolute;left:28px;top:170px}
  .services__list li{list-style:none;display:flex;align-items:center;gap:12px;font-family:"Barlow Condensed",sans-serif;font-size:16.5px;height:28px;color:#333}
  .services__list svg{width:18px;height:18px;color:var(--green)}
  .services__footer{position:absolute;left:0;top:555px;width:340px;height:135px;background:var(--green)}
  .services__grid{position:absolute;left:28px;top:408px;width:226px;height:172px;background:var(--white);display:grid;grid-template-columns:1fr 1fr;grid-template-rows:1fr 1fr;gap:4px;padding:0 4px 4px 0}
  .tile-text{background:var(--green);color:var(--white);display:flex;align-items:center;justify-content:center;text-align:center;font-weight:600;font-style:italic;font-size:9.5px;line-height:1.45;margin-top:10px}
  .grid-photo{position:relative}
  .grid-photo--kitchen{background:linear-gradient(135deg,#d8dde0,#b9a58e)}
  .grid-photo--branch{background:linear-gradient(135deg,#9bb37d,#5a7a45)}
  .grid-photo--floor{background:linear-gradient(135deg,#cfcac3,#e7e3de)}
  .contact{position:absolute;left:0;top:593px;width:340px;text-align:center;color:var(--white);font-size:10.5px;line-height:1.6}
  .contact__company{font-weight:700;font-size:11px;margin-bottom:4px}
  .contact strong{font-weight:700}
</style>
</head>
<body>
<svg class="icon-defs" aria-hidden="true">
  <defs>
    <symbol id="icon-tick" viewBox="0 0 24 24">
      <path d="M19 8.5A9 9 0 1 1 15.5 4.3" fill="none" stroke="currentColor" stroke-width="2.4" stroke-linecap="round"/>
      <path d="M7 11.5l4 4L22 4" fill="none" stroke="currentColor" stroke-width="2.8" stroke-linecap="round" stroke-linejoin="round"/>
    </symbol>
  </defs>
</svg>

<article class="flyer flyer--haccp">
  <div class="photo haccp__hero" role="img" aria-label="Foto: Mitarbeiterin in weißer Hygienekleidung mit Tablet in einer Lebensmittelproduktion"></div>
  <div class="brand">
    <div class="brand__name">Schädlingsfrei<br>Jonas Karwolt<br>Bad Lindenfeld</div>
    <span class="brand__mark"></span>
  </div>
  <div class="haccp__band"></div>
  <div class="haccp__title">HAACP<br>Service</div>
  <section class="haccp__intro">
    <h2>Was ist HACCP?</h2>
    <p>HACCP ist der systematische Ansatz, den wir anwenden, um unbedenkliche Lebensmittel zu gewährleisten. Die Aufgabe des HACCP-Konzeptes ist es, Gefahren, die mit dem Verarbeitungsprozess von Lebensmitteln zusammenhängen oder von fertigen Produkten ausgehen, zu betrachten und die Risiken abzuschätzen. Wenn alle Faktoren, die die Lebensmittelsicherheit beeinträchtigen können, erkannt sind, dann können die entsprechenden Maßnahmen zum Einsatz kommen, um diese Risikofaktoren auszuschalten.</p>
  </section>
  <section class="haccp__steps">
    <h3>Wie wird das HACCP-Konzept eingesetzt?</h3>
    <ul>
      <li>Schritt 1 – Verfahren und Produkt definieren</li>
      <li>Schritt 2 – Risikofaktoren identifizieren</li>
      <li>Schritt 3 – Risikoträchtige Prozessabschnitte bestimmen</li>
      <li>Schritt 4 – Risikoträchtige Prozessabschnitte überwachen</li>
      <li>Schritt 5 – Risikoträchtige Prozessabschnitte dokumentieren</li>
      <li>Schritt 6 – System zur Fehlerkorrektur</li>
      <li>Schritt 7 – HACCP-System auf Wirksamkeit prüfen</li>
    </ul>
  </section>
  <div class="haccp__benefits">
    <div class="benefit"><svg><use href="#icon-tick"/></svg><span>fachgerechte<br>Bekämpfung mit<br>Erfahrung</span></div>
    <div class="benefit"><svg><use href="#icon-tick"/></svg><span>schnell,<br>nachhaltig<br>und einfach</span></div>
  </div>
  <div class="footer-bar">www.skw-bl.de</div>
</article>

<article class="flyer flyer--services">
  <div class="brand">
    <div class="brand__name">Schädlingsfrei<br>Jonas Karwolt<br>Bad Lindenfeld</div>
    <span class="brand__mark"></span>
  </div>
  <h2 class="services__lead">Ihr Fachbetrieb in Bad Lindenfeld für:</h2>
  <ul class="services__list">
    <li><svg><use href="#icon-tick"/></svg>Holz- und Bautenschutz</li>
    <li><svg><use href="#icon-tick"/></svg>Hausbockbekämpfung</li>
    <li><svg><use href="#icon-tick"/></svg>Hausschwammbekämpfung</li>
    <li><svg><use href="#icon-tick"/></svg>Pilz/ Schimmelpilzsanierung</li>
    <li><svg><use href="#icon-tick"/></svg>Schädlingsbekämpfung</li>
    <li><svg><use href="#icon-tick"/></svg>Taubenabwehr</li>
    <li><svg><use href="#icon-tick"/></svg>HACCP Service</li>
  </ul>
  <div class="services__footer"></div>
  <div class="services__grid">
    <div class="grid-photo grid-photo--kitchen" role="img" aria-label="Foto: Schädlingsbekämpfer in Schutzanzug sprüht in einer Küche"></div>
    <div class="tile-text">Schädlings-<br>bekämpfung,<br>Holz- und Bauten-<br>schutz</div>
    <div class="grid-photo grid-photo--branch" role="img" aria-label="Foto: Sprühbehandlung eines grünen Zweiges"></div>
    <div class="grid-photo grid-photo--floor" role="img" aria-label="Foto: Fachkraft behandelt Fußleiste mit Schädlingsbefall"></div>
  </div>
  <address class="contact" style="font-style:normal">
    <div class="contact__company">Schädlingsfrei Jonas Karwolt – Bad Lindenfeld</div>
    <div>Ahornweg 14 | 55590 Bad Lindenfeld</div>
    <div><strong>Mobil:</strong> 0152/48201937 | <strong>Email:</strong> karwolt(at)skw-bl.de</div>
  </address>
  <div class="footer-bar" style="border-radius:18px 18px 0 0">www.skw-bl.de</div>
</article>
</body>
</html>
```